Geschäftspapiere für ein Bauunternehmen
Zielgruppe
Meine Firma ist ein Bauunternehmen und suchen ein Modernes aber auch hochwertiges Design für unsere Geschäftspapiere und unsere Zielgruppen sind Private Kunden die ein oder mehrere Häuser bauen wollen.
Aufgabenstellung
Das Design soll sehr modern aber auch hochwertig sein.

```html
<!DOCTYPE html>
<html lang="de">
<head>
<meta charset="utf-8">
<title>Kessler Bau – Briefbogen</title>
<link href="https://fonts.googleapis.com/css2?family=Open+Sans:wght@400;600;700&display=swap" rel="stylesheet">
<style>
  :root {
    --bg: #e9eaea;
    --paper: #ffffff;
    --ink: #2b2b2b;
    --ink-soft: #3a3a3a;
    --accent: #c4393a;
    --rule: #c9c9c9;
    --ghost: #f6f6f6;
  }
  * { margin: 0; padding: 0; box-sizing: border-box; }
  html, body { width: 1151px; height: 1200px; overflow: hidden; }
  body {
    background: var(--bg);
    font-family: "Open Sans", Arial, sans-serif;
    color: var(--ink);
    position: relative;
  }
  .letterhead {
    position: absolute;
    left: 172px; top: 30px;
    width: 806px; height: 1140px;
    background: var(--paper);
  }
  .letterhead > * { position: absolute; }

  .brand {
    right: 54px; top: 150px;
    display: flex; align-items: center; gap: 10px;
  }
  .brand-square { width: 22px; height: 22px; background: var(--accent); }
  .brand-name {
    font-weight: 700; font-size: 22px; letter-spacing: 1.5px; color: var(--ink);
  }

  .sender-line {
    left: 97px; top: 200px;
    font-size: 7.5px; color: var(--ink-soft);
    border-bottom: 1px solid var(--ink-soft);
    padding-bottom: 1px; white-space: nowrap;
  }
  .sender-line .sep { color: var(--accent); margin: 0 3px; }

  .recipient {
    left: 97px; top: 238px;
    font-size: 12px; line-height: 17px;
  }
  .recipient .city { margin-top: 16px; }

  .contact {
    left: 608px; top: 219px; height: 112px;
    border-left: 1px solid var(--ink-soft);
    padding-left: 12px;
    font-size: 10.5px; line-height: 15px; white-space: nowrap;
  }
  .contact-list { list-style: none; margin-top: 12px; }
  .contact-list li { display: flex; align-items: center; gap: 6px; }
  .contact-list svg { width: 10px; height: 10px; fill: var(--accent); flex: none; }

  .fold-mark { left: 0; width: 24px; height: 1px; background: var(--rule); }
  .fold-mark.top { top: 404px; }
  .fold-mark.mid { top: 570px; }
  .fold-mark.low { top: 807px; }

  .watermark {
    left: 0; right: 0; top: 560px;
    text-align: center;
    font-weight: 700; font-size: 96px; letter-spacing: 4px;
    color: var(--ghost);
  }

  .footer {
    left: 98px; right: 54px; top: 1084px;
    display: flex; align-items: center;
    font-size: 10.5px; line-height: 15px;
  }
  .footer-col { white-space: nowrap; }
  .footer-col.bank { width: 179px; }
  .footer-col.tax { width: 251px; padding-left: 36px; }
  .footer-col.account { padding-left: 36px; }
  .footer-divider { width: 1px; height: 29px; background: var(--ink-soft); }
</style>
</head>
<body>
  <main class="letterhead">
    <div class="brand">
      <span class="brand-square"></span>
      <span class="brand-name">KESSLERBAU</span>
    </div>

    <p class="sender-line">Kessler Bau GmbH<span class="sep">|</span>Muster Weg 32<span class="sep">|</span>10400 Muster Stadt</p>

    <address class="recipient" style="font-style:normal">
      <p>Musterfirma</p>
      <p>z. Hd. Herrn Mustermann</p>
      <p>Musterweg 13</p>
      <p class="city">24102 Musterstadt</p>
    </address>

    <address class="contact" style="font-style:normal">
      <p>Kessler Bau GmbH</p>
      <p>Muster Weg 32</p>
      <p>10400 Muster Stadt</p>
      <ul class="contact-list">
        <li><svg viewBox="0 0 10 10"><path d="M2 0.5 L3.6 2.6 L2.7 3.6 Q3.6 5.6 6.4 7.3 L7.4 6.4 L9.5 8 L8.3 9.5 Q2.5 8.5 0.5 1.7 Z"/></svg>+49 (0) 555 010 204 10</li>
        <li><svg viewBox="0 0 10 10"><rect x="2.5" y="0.5" width="5" height="3"/><rect x="0.5" y="3.5" width="9" height="4"/><rect x="2.5" y="7" width="5" height="2.5"/></svg>+49 (0) 555 010 204 19</li>
        <li><svg viewBox="0 0 10 10"><path d="M0.5 2 H9.5 V8.5 H0.5 Z M1 2.4 L5 5.6 L9 2.4" stroke="#fff" stroke-width="0.8"/></svg>info@kesslerbau.de</li>
        <li><svg viewBox="0 0 10 10"><circle cx="5" cy="5" r="4.5"/></svg>www.kesslerbau.de</li>
      </ul>
    </address>

    <span class="fold-mark top"></span>
    <span class="fold-mark mid"></span>
    <span class="fold-mark low"></span>

    <p class="watermark" aria-hidden="true">KESSLERBAU</p>

    <footer class="footer">
      <div class="footer-col bank">
        <p>Bankverbindung:</p>
        <p>Sparkasse Talgrund-Nord</p>
      </div>
      <span class="footer-divider"></span>
      <div class="footer-col tax">
        <p>Steuernummer: 204/311/00000</p>
        <p>Umsatzsteuer-ID-Nr.: DE 000123456</p>
      </div>
      <span class="footer-divider"></span>
      <div class="footer-col account">
        <p>BIC: TALGDE21XXX</p>
        <p>IBAN: DE00 1234 5678 9012 00000 00</p>
      </div>
    </footer>
  </main>
</body>
</html>
```